Create a Wordpress website and online store for a car performance shop

-Website to be coded in Wordpress AFTER design and be an WooCommerce store (will increase to a proper budget for coding after design has been finalised/picked)

-We are a car performance shop that is offering mechanical services + selling parts online

Industry/Entity Type

Automotive

Logo Text

Brisk Automotive

Number of Pages Required

3 page

Colors
e24097
e667a6
eea4c8
fff9f9

Requirements
Must have
• - Wordpress with WooCommerce store
• - Similar website/store design to what i want - https://kestrunparts.com/default.aspx
• See Website script.docx attached.
• I don't want it to be exact copy but it is a inspiration of what i want my website to look/feel.
• - LOGO must be playful using the colours picked - see attached SAMPLE LOGOS.jpg

```html
<!DOCTYPE html>
<html lang="en">
<head>
<meta charset="utf-8">
<title>Brisk Automotive</title>
<link href="https://fonts.googleapis.com/css2?family=Montserrat:wght@400;500;600;700;800&display=swap" rel="stylesheet">
<style>
:root{
  --pink:#e24097;
  --pink-mid:#e667a6;
  --pink-soft:#eea4c8;
  --blush:#fff9f9;
  --ink:#1d1c22;
  --text:#2b2b33;
  --line:#d9d9de;
  --white:#ffffff;
}
*{margin:0;padding:0;box-sizing:border-box}
html,body{width:879px;height:1200px;overflow:hidden;background:var(--white)}
body{position:relative;font-family:'Montserrat',sans-serif;color:var(--text)}
.abs{position:absolute}
.topbar{left:0;top:0;width:879px;height:16px;background:var(--ink);color:#fff;font-size:6.2px}
.topbar span{position:absolute;top:4.5px}
.header{left:0;top:16px;width:879px;height:97px;background:var(--blush);border-bottom:1px solid #eee}
.logo{font-weight:800;color:var(--pink);font-size:17px;letter-spacing:-.3px;white-space:nowrap}
.logo.head{left:182px;top:45px;width:138px;font-size:14px;letter-spacing:-.4px}
.search{left:330px;top:41px;width:220px;height:22px;border:1px solid #e5dede;border-radius:11px;background:#fff;font-size:6px;padding:8px 12px;color:#333}
.search-btn{left:496px;top:41px;width:54px;height:22px;background:var(--pink);color:#fff;border-radius:0 11px 11px 0;font-size:6px;font-weight:700;text-align:center;line-height:22px}
.hdr-link{font-size:7px;line-height:9px}
.hdr-link b{font-weight:600}
.cat-tab{left:182px;top:88px;width:147px;height:25px;background:linear-gradient(var(--pink-mid),var(--pink));border-radius:4px 4px 0 0;color:#fff;font-weight:700;font-size:11px;text-align:center;line-height:25px}
.nav{top:97px;font-size:6.4px;color:#222}
.mega{left:182px;top:113px;width:515px;height:236px;background:var(--pink);border-radius:0 0 4px 4px}
.mega-list{left:209px;top:127px;font-size:7.8px;color:var(--pink-soft);line-height:17.6px}
.mega-list .on{color:#fff;font-weight:700}
.scroll{left:190px;top:141px;width:2.5px;height:120px;background:#fff;border-radius:2px}
.tile{width:87px;height:60px;background:#fff;border-radius:2px;padding:6px}
.tile.sel{outline:1.5px solid var(--ink)}
.tile .ph{width:100%;height:100%;background:radial-gradient(circle at 50% 50%,#bdbdc2,#f1f1f3 70%);border-radius:2px}
.load{left:475px;top:318px;width:71px;height:20px;background:var(--ink);color:#fff;border-radius:10px;font-size:8px;font-weight:700;text-align:center;line-height:20px}
.side{left:182px;width:147px;height:23.5px;border:1px solid var(--line);border-radius:3px;font-size:8.4px;padding:0 12px;line-height:22px;background:#fff}
.side.active{background:var(--pink);color:#fff;font-weight:700;border-color:var(--pink)}
.side svg{position:absolute;right:9px;top:8px}
.sub{left:195px;top:432px;font-size:7.2px;line-height:14.2px}
.sub li{list-style:none}
.sub li::before{content:"•";color:var(--pink);margin-right:7px}
.brand{width:86px;height:47px;border:1px solid var(--line);text-align:center;background:#fff}
.brand.sel{border-color:var(--pink)}
.brand .mark{display:block;margin-top:9px;font-weight:800;font-size:10px;color:var(--pink)}
.brand .name{display:block;margin-top:7px;font-size:6.3px}
.banner{left:342px;top:524px;width:354px;height:123px;border-radius:4px;overflow:hidden;background:linear-gradient(90deg,#f4f4f6 0%,#eaa9c9 40%,var(--pink) 65%)}
.banner .ph{left:0;top:0;width:160px;height:123px;background:radial-gradient(ellipse at 45% 55%,#3a3a40 0%,#7d7d84 40%,rgba(255,255,255,0) 75%)}
.featured{left:342px;top:678px;width:354px;height:23px;background:var(--pink);color:#fff;font-weight:700;font-size:8.2px;padding:6px 11px;border-radius:3px 3px 0 0}
.card{width:115px;height:100px;border:1px solid var(--line);top:704px}
.card .ph{left:20px;top:14px;width:74px;height:52px;background:radial-gradient(ellipse,#8b8b92,#e7e7ea 70%,#fff 100%)}
.card .stars{left:10px;top:85px;font-size:6.5px;color:var(--pink);letter-spacing:.6px}
.card .stars i{font-style:normal;color:var(--ink)}
.price{top:815px;color:var(--pink);font-weight:700;font-size:8.2px}
.ptitle{top:826px;font-size:8.2px}
.pdesc{top:843px;font-size:5.2px;line-height:8px;width:110px}
.btn{top:864px;width:53px;height:16px;border-radius:8px;font-size:5.8px;font-weight:700;text-align:center;line-height:14px}
.btn.fill{background:var(--pink);color:#fff;border:1px solid var(--pink)}
.btn.line{border:1px solid var(--ink);color:var(--ink)}
.footer{left:0;top:919px;width:879px;height:281px;background:var(--ink);color:#fff;overflow:hidden}
.brush{background:linear-gradient(135deg,#fff 0%,#f3d1e2 45%,var(--pink-mid) 100%);opacity:.95}
.f-head{top:100px;font-weight:700;font-size:8px;color:var(--pink)}
.f-col{top:130px;font-size:7.2px;line-height:16.3px}
.f-about{left:181px;top:115px;width:135px;font-size:7px;line-height:9.4px;font-weight:500}
.f-contact{left:181px;top:165px;font-size:7px;line-height:14px}
.f-contact em{font-style:normal;color:var(--pink)}
.news{left:564px;top:151px;width:132px;height:22px;border:1px solid #fff;border-radius:11px;font-size:7px;padding:6px 9px}
.pay{top:187px;width:22px;height:15px;border-radius:2px}
.rule{left:182px;top:230px;width:515px;height:1px;background:#3a3940}
.copy{left:0;top:247px;width:879px;text-align:center;font-size:6.2px;font-weight:500}
</style>
</head>
<body>

<div class="abs topbar">
  <span style="left:182px">Contact Us</span>
  <span style="left:229px">News</span>
  <span style="left:259px">Blog</span>
  <svg class="abs" style="left:371px;top:4px" width="9" height="8" viewBox="0 0 9 8"><path d="M1 3C1 1 3 1 4.5 1S8 1 8 3L6.5 3.5 6 2.5H3L2.5 3.5ZM2 4H7L7.5 7.5H1.5Z" fill="#e24097"/></svg>
  <span style="left:385px">Call Us:(+0)000 000 0000</span>
  <svg class="abs" style="left:471px;top:4.5px" width="9" height="7" viewBox="0 0 9 7"><rect width="9" height="7" fill="#e24097"/><path d="M0 0L4.5 4 9 0" stroke="#fff" stroke-width=".8" fill="none"/></svg>
  <span style="left:487px">info@briskautomotive.com</span>
  <svg class="abs" style="left:666px;top:4px" width="8" height="8" viewBox="0 0 8 8"><rect x="3" y="0.5" width="4.5" height="7" fill="none" stroke="#e24097"/><path d="M0 4H4M2.5 2.5L4 4 2.5 5.5" stroke="#e24097" fill="none"/></svg>
  <span style="left:678px">Log In</span>
</div>

<div class="abs header"></div>
<div class="abs logo head">Brisk Automotive</div>
<div class="abs search">Serach for products...</div>
<div class="abs search-btn">SERACH</div>
<svg class="abs" style="left:564px;top:44px" width="18" height="17" viewBox="0 0 18 17"><path d="M0 2H3L5 11H14L16 4H4" stroke="#e24097" stroke-width="1.6" fill="none"/><circle cx="6" cy="14" r="1.6" fill="#e24097"/><circle cx="13" cy="14" r="1.6" fill="#e24097"/><circle cx="16" cy="3" r="3.5" fill="#1d1c22"/><text x="16" y="4.6" font-size="4.5" fill="#fff" text-anchor="middle" font-family="Montserrat,sans-serif">2</text></svg>
<div class="abs hdr-link" style="left:589px;top:43px">Shopping<br><b>Cart</b></div>
<svg class="abs" style="left:638px;top:44px" width="12" height="15" viewBox="0 0 12 15"><circle cx="6" cy="4" r="3" fill="#e24097"/><path d="M0 15C0 9 12 9 12 15Z" fill="#e24097"/></svg>
<div class="abs hdr-link" style="left:653px;top:43px">Sign in<br><b>My Account</b></div>

<div class="abs cat-tab">Categories <svg width="8" height="6" viewBox="0 0 8 6" style="margin-left:6px"><path d="M1 1L4 4 7 1" stroke="#fff" stroke-width="1.4" fill="none"/></svg></div>
<div class="abs nav" style="left:367px">Home</div>
<div class="abs nav" style="left:413px">Ostmark OT Series Kit Builder <span style="color:var(--pink)">⌄</span></div>
<div class="abs nav" style="left:531px">Manufacturers <span style="color:var(--pink)">⌄</span></div>
<div class="abs nav" style="left:603px">Customer Service <span style="color:var(--pink)">⌄</span></div>

<div class="abs mega"></div>
<svg class="abs" style="left:189px;top:122px" width="7" height="5" viewBox="0 0 7 5"><path d="M1 4L3.5 1.5 6 4" stroke="#fff" stroke-width="1.2" fill="none"/></svg>
<div class="abs scroll"></div>
<svg class="abs" style="left:189px;top:336px" width="7" height="5" viewBox="0 0 7 5"><path d="M1 1L3.5 3.5 6 1" stroke="#fff" stroke-width="1.2" fill="none"/></svg>
<div class="abs mega-list">
  <div>Adhesives</div><div>Battery Boots</div><div>Clearance Items</div><div>Expandable Sleeving</div>
  <div class="on">Fuse Blocks/Holders</div><div>Indicators</div><div>Junction Blocks</div><div>Relays</div>
  <div>Aircraft / Automotive Wire</div><div>Wire Connectors</div><div>Circuit Breakers</div><div>Cable Ties</div>
</div>

<div class="abs tile" style="left:330px;top:118px"><div class="ph" role="img" aria-label="Adhesive dispensing gun"></div></div>
<div class="abs tile" style="left:421px;top:118px"><div class="ph" role="img" aria-label="Assorted battery boots"></div></div>
<div class="abs tile" style="left:512px;top:118px"><div class="ph" role="img" aria-label="Indicator lamps"></div></div>
<div class="abs tile" style="left:604px;top:118px"><div class="ph" role="img" aria-label="Circular connector"></div></div>
<div class="abs tile sel" style="left:330px;top:182px"><div class="ph" role="img" aria-label="Fuse holders"></div></div>
<div class="abs tile" style="left:421px;top:182px"><div class="ph" role="img" aria-label="Ring terminals"></div></div>
<div class="abs tile" style="left:512px;top:182px"><div class="ph" role="img" aria-label="Toggle switches"></div></div>
<div class="abs tile" style="left:604px;top:182px"><div class="ph" role="img" aria-label="Stripped cable wires"></div></div>
<div class="abs tile" style="left:330px;top:246px"><div class="ph" role="img" aria-label="Cable label roll in box"></div></div>
<div class="abs tile" style="left:421px;top:246px"><div class="ph" role="img" aria-label="Spool of wire"></div></div>
<div class="abs tile" style="left:512px;top:246px"><div class="ph" role="img" aria-label="Connector kit with pins"></div></div>
<div class="abs tile" style="left:604px;top:246px"><div class="ph" role="img" aria-label="Heat shrink boots"></div></div>
<div class="abs load">Load More</div>

<div class="abs side" style="top:350px">Battery Boots</div>
<div class="abs side" style="top:372px">Clearance Items</div>
<div class="abs side active" style="top:398px">Expandable Sleeving<svg width="7" height="5" viewBox="0 0 7 5"><path d="M1 1L3.5 3.5 6 1" stroke="#fff" stroke-width="1.2" fill="none"/></svg></div>
<ul class="abs sub"><li>Flex-Sleeve F Series</li><li>Split Braid Sleeve</li><li>Flex-Sleeve Non Fray Series</li></ul>
<div class="abs side" style="top:499px">Fuse Blocks/Holders</div>
<div class="abs side" style="top:525px">Indicators</div>
<div class="abs side" style="top:550px">Junction Blocks</div>
<div class="abs side" style="top:576px">Relays</div>
<div class="abs side" style="top:601px">Aircraft / Automotive Wire<svg width="7" height="5" viewBox="0 0 7 5"><path d="M1 1L3.5 3.5 6 1" stroke="#e24097" stroke-width="1.2" fill="none"/></svg></div>
<div class="abs side" style="top:627px">Wire Connectors<svg width="7" height="5" viewBox="0 0 7 5"><path d="M1 1L3.5 3.5 6 1" stroke="#e24097" stroke-width="1.2" fill="none"/></svg></div>
<div class="abs side" style="top:652px">Circuit Breakers<svg width="7" height="5" viewBox="0 0 7 5"><path d="M1 1L3.5 3.5 6 1" stroke="#e24097" stroke-width="1.2" fill="none"/></svg></div>
<div class="abs side" style="top:678px">Cable Ties</div>
<div class="abs side" style="top:703px">Heat Shrink Tubing<svg width="7" height="5" viewBox="0 0 7 5"><path d="M1 1L3.5 3.5 6 1" stroke="#e24097" stroke-width="1.2" fill="none"/></svg></div>
<div class="abs side" style="top:729px">Heat Shrink Boots<svg width="7" height="5" viewBox="0 0 7 5"><path d="M1 1L3.5 3.5 6 1" stroke="#e24097" stroke-width="1.2" fill="none"/></svg></div>
<div class="abs side" style="top:754px">Switches<svg width="7" height="5" viewBox="0 0 7 5"><path d="M1 1L3.5 3.5 6 1" stroke="#e24097" stroke-width="1.2" fill="none"/></svg></div>
<div class="abs side" style="top:780px">Tools</div>
<div class="abs side" style="top:805px">Terminal Connectors<svg width="7" height="5" viewBox="0 0 7 5"><path d="M1 1L3.5 3.5 6 1" stroke="#e24097" stroke-width="1.2" fill="none"/></svg></div>
<div class="abs side" style="top:831px">Motrix</div>
<div class="abs side" style="top:857px">Loom Supplies</div>

<div class="abs brand" style="left:342px;top:350px"><span class="mark">NORDA</span><span class="name">Norda</span></div>
<div class="abs brand" style="left:432px;top:350px"><span class="mark">ARCLINE</span><span class="name">Arcline</span></div>
<div class="abs brand" style="left:521px;top:350px"><span class="mark">TIDEWELL</span><span class="name">Tidewell Systems</span></div>
<div class="abs brand" style="left:611px;top:350px"><span class="mark">HALVORN</span><span class="name">Halvorn</span></div>
<div class="abs brand" style="left:342px;top:398px"><span class="mark">RAVELLE</span><span class="name">Ravelle</span></div>
<div class="abs brand" style="left:432px;top:398px"><span class="mark">BRENNAN</span><span class="name">Brennan MFG</span></div>
<div class="abs brand sel" style="left:521px;top:398px"><span class="mark">CORVENT</span><span class="name">Corvent</span></div>
<div class="abs brand" style="left:611px;top:398px"><span class="mark">OSTMARK</span><span class="name">Ostmark Autosport</span></div>
<div class="abs brand" style="left:342px;top:450px"><span class="mark">LUMIRA</span><span class="name">Lumira</span></div>
<div class="abs brand" style="left:432px;top:450px"><span class="mark">KESSA</span><span class="name">Kessa</span></div>
<div class="abs brand" style="left:521px;top:450px"><span class="mark">FAIRLOCK</span><span class="name">Fairlock</span></div>
<div class="abs brand" style="left:611px;top:450px"><span class="mark">VEYRA</span><span class="name">Veyra</span></div>

<div class="abs banner">
  <div class="abs ph" role="img" aria-label="Assorted black heat shrink boots and moulded parts"></div>
  <div class="abs" style="right:16px;top:26px;color:#fff;font-weight:700;font-size:20px;text-align:right;line-height:22px">Voltra<br><span style="font-size:9px">linkage</span></div>
  <div class="abs" style="right:16px;top:88px;color:var(--ink);font-weight:700;font-size:18px">Thermwrap</div>
</div>

<div class="abs featured">Featured Products</div>

<div class="abs card" style="left:342px"><div class="abs ph" role="img" aria-label="Coilover suspension set"></div><div class="abs stars">★★★★<i>★</i></div></div>
<div class="abs card" style="left:462px"><div class="abs ph" role="img" aria-label="Gearbox transmission"></div><div class="abs stars">★★★★<i>★</i></div></div>
<div class="abs card" style="left:582px"><div class="abs ph" role="img" aria-label="Pair of projector headlights"></div><div class="abs stars">★★★★<i>★</i></div></div>

<div class="abs price" style="left:342px">$296.00</div>
<div class="abs ptitle" style="left:342px">Headlight Vanta Lumo 6N</div>
<div class="abs pdesc" style="left:342px">So, if you like listening to the sound of your engine.</div>
<div class="abs btn fill" style="left:342px">Add to Cart</div>
<div class="abs btn line" style="left:399px">Details</div>

<div class="abs price" style="left:463px">$296.00</div>
<div class="abs ptitle" style="left:463px">Headlight Vanta Lumo 6N</div>
<div class="abs pdesc" style="left:463px">So, if you like listening to the sound of your engine.</div>
<div class="abs btn fill" style="left:463px">Add to Cart</div>
<div class="abs btn line" style="left:520px">Details</div>

<div class="abs price" style="left:586px">$296.00</div>
<div class="abs ptitle" style="left:586px">Headlight Vanta Lumo 6N</div>
<div class="abs pdesc" style="left:586px">So, if you like listening to the sound of your engine.</div>
<div class="abs btn fill" style="left:586px">Add to Cart</div>
<div class="abs btn line" style="left:644px">Details</div>

<div class="abs footer">
  <div class="abs brush" role="img" aria-label="Brush stroke texture" style="left:-40px;top:40px;width:180px;height:230px;transform:rotate(-18deg);border-radius:40px 10px 60px 20px"></div>
  <div class="abs brush" role="img" aria-label="Brush stroke texture" style="left:750px;top:30px;width:170px;height:240px;transform:rotate(20deg);border-radius:20px 50px 10px 60px;background:linear-gradient(135deg,var(--pink-mid),#fff 60%,var(--pink) 100%)"></div>

  <div class="abs logo" style="left:0;width:879px;text-align:center;top:37px;font-size:18px">Brisk Automotive</div>

  <div class="abs f-head" style="left:181px">ABOUT US</div>
  <div class="abs f-about">Lorem ipsum dolor sit amet, consectetur elit. Ad assumenda fuga illo laudantium magni sed temporibus fuga illo laudantium.</div>
  <div class="abs f-contact"><em>Address:</em> ABC Street City 12345<br><em>Phone:</em> +00 000 000 0000<br><em>E-mail:</em> info@briskautomotive.com</div>

  <div class="abs f-head" style="left:345px">My Account</div>
  <div class="abs f-col" style="left:345px">My Account<br>My Wishlist<br>My Orders<br>Order Tracking<br>Shipping Info</div>

  <div class="abs f-head" style="left:451px">My Service</div>
  <div class="abs f-col" style="left:451px">Order History<br>Personal Information<br>Check Out<br>Shipping Cart<br>Login/Register</div>

  <div class="abs f-head" style="left:563px">Newsletter</div>
  <div class="abs" style="left:563px;top:120px;width:140px;font-size:7px;line-height:14px">Sign up with your email to get fresh updates.</div>
  <div class="abs news">Enter your email address</div>
  <svg class="abs" style="left:681px;top:159px" width="8" height="6" viewBox="0 0 8 6"><rect width="8" height="6" fill="#e24097"/><path d="M0 0L4 3.5 8 0" stroke="#fff" stroke-width=".7" fill="none"/></svg>
  <div class="abs pay" style="left:569px;background:#fff"></div>
  <div class="abs pay" style="left:599px;background:#2a2f7a"></div>
  <div class="abs pay" style="left:629px;background:#3aa0dc"></div>
  <div class="abs pay" style="left:659px;background:#f4f4f4"></div>

  <div class="abs rule"></div>
  <div class="abs copy">Copyright © 2020 Brisk Automotive. All Rights Reserved. &nbsp;| &nbsp;Built By Northpine Studio</div>
</div>

</body>
</html>
```